The Grove- All Natural Company Needs Packaging for Main Product

Aloha!

We are a natural products company from Kaua’i, Hawaii called “The Grove”

The first thing we need packaging for is for our all natural bug spray called “Natural Pest Ward”

We will need much more packaging for many other products in the future so we need a packaging design theme that will serve many products. Our other products are a Reef Safe Sunblock Face Stick called Face Shade
Reef Safe Sunblock Body Lotion called Body Shade and other future natural products.

Very Important:
We love all Tide Pup packaging for its simplicity and cleanness. We honestly want our packaging to be just like Tide Pup in its own way. Instead of having the monkey, we want our Grove logo to go in the middle like the monkey is on all Tide Pup packaging. We want everything else pretty much the same but just for Bug Spray. Though, we do not want to copy of course, but we would like it be similar.

Front Label- Needs to be on there: (Following guide of Tide Pup Front label)
1. Black Background
2. Grove logo
3. Make it look professional
4. Make it Clean
5. Make it pop on the shelf
6. Needs to say the following:

** Please not we changed the brief. We changed it so Natural Pest Ward all goes together on the front as one logo for
Natural
Bug
Grove

a. Natural Pest Ward (where Tide Pup is)
b. Grove Logo (where monkey is)
c. Deet-Free. (where Golden Blend is)
d. Bug Spray (in between 2 lines) (where Tress Brightener is)
e. Natural Bug Spray enriched (where it says Premium Hair enriched…)
with quality essential oils that
repels mosquitos, gnats, no seeums,
ticks and all other bitey things.
f. Made with Aloha (where it says Blonde to Medium Brown Hair Types)
g. 4 FL OZ/ 118 mL (under Blonde to Medium Brown Hair Types)

Back Label-Things need on there: (Following guide of Tide Pup Back Label)

1. We have given an example Tide Pup Back Label. We would like it to look very similar to it.
2. Make room for a small UPC code on back.
3. Needs to say:

The Grove products are naturally made for those to enjoy the outdoors.

Reef Safe Gluten Free Hypoallergenic Non-GMO
Deet Free Paraben Free Gluten Free Organic Ingredients

Product Description

Pest Ward is naturally enriched with quality essential oils to repel mosquitos, gnats, no seeums, ticks, and all other bites things. It is safe for babies, kids, and adults.

How to Use

Shake well and spray well on all parts of the body. Reapply every hour while outside.

Warning

Do not spray near or in eyes. If mistakenly sprayed in eyes, rinse with running water for 30 minutes.

Ingredients

Active Ingredients: Cedar wood oil (.35%) Citronella Oil (.30%) Eucalyptus Oil (.20%) Lemongrass Oil (.20%) Lavender Oil (.20%)
Inert Ingredients: Distilled Water, Coconut Oil, Witch Hazel

Exclusively Manufactured and Distributed by The Grove LLC, 2836 Wainohe Rd. Kilauea, Hawaii, 96754 USA © All Rights Reserved
Get more information at NaturalPestWard.example

Other Notes.
1. The label we’ve been using is 4”x5”
2. The Font we've been using for the Pest Ward logo part is Neutraface but we are glad to try other things that would make it look clean and stand out. Love the Tide Pup logo and font but definitely want something unique for us.

Attached:

Thank you for all your hard work on this project. Please let us know if you have any questions, and we look forward to seeing your amazing packaging design.

Thanks and Aloha!
The Grove Team

Target Market(s)

Retail Stores, Adventure Tours, Families

Industry/Entity Type

It Company

Font styles to use
Other font styles liked:
• Professional looking font

Colors
e34196
fbed22
00a990
000000
fbfbfb

Requirements
Must have
• Wrote everything above.
• Must Be VERY professional.
• Clean look.
• POP on a shelf.
• Creative
• White lettering to make it look clean with black background.
Nice to have
• Wrote everything above.
• Must be VERY professional.
• Clean look
• POP on a shelf
• Creative
Should not have
• Clutter
• not look professional
• distractions

```html
<!DOCTYPE html>
<html lang="en">
<head>
<meta charset="utf-8">
<title>Natural Pest Ward – Bug Spray Front Label</title>
<link rel="stylesheet" href="https://fonts.googleapis.com/css2?family=Montserrat:wght@800&family=Roboto+Condensed:wght@300;400&family=Playfair+Display:wght@900&display=swap">
<style>
  :root {
    --label-black: #121212;
    --ink-white: #fbfbfb;
    --aloha-yellow: #fbed22;
    --rule-yellow: #e2e02a;
    --leaf-green: #00a990;
    --hibiscus-pink: #e34196;
    --body-grey: #d8d8d8;
  }
  * { margin: 0; padding: 0; box-sizing: border-box; }
  html, body {
    width: 730px;
    height: 1200px;
    overflow: hidden;
    background: var(--label-black);
  }
  .label {
    position: relative;
    width: 730px;
    height: 1200px;
    background: var(--label-black);
    color: var(--ink-white);
    text-align: center;
  }
  .wordmark {
    position: absolute;
    top: 130px;
    left: 0;
    width: 100%;
    font-family: "Montserrat", sans-serif;
    font-weight: 800;
    color: var(--ink-white);
    line-height: 0.92;
  }
  .wordmark__natural {
    display: block;
    font-size: 34px;
    letter-spacing: 2px;
    text-transform: lowercase;
    margin-bottom: 8px;
  }
  .wordmark__line {
    display: block;
    font-size: 104px;
    letter-spacing: -1px;
  }
  .wordmark__line--small { font-size: 92px; }
  .brand-mark {
    position: absolute;
    top: 440px;
    left: 0;
    width: 100%;
    display: flex;
    justify-content: center;
    align-items: center;
    gap: 18px;
  }
  .brand-mark__square {
    width: 56px;
    height: 56px;
    background: var(--hibiscus-pink);
  }
  .brand-mark__name {
    font-family: "Montserrat", sans-serif;
    font-weight: 800;
    font-size: 52px;
    color: var(--ink-white);
  }
  .claim {
    position: absolute;
    top: 700px;
    left: 0;
    width: 100%;
    font-family: "Roboto Condensed", sans-serif;
    font-weight: 400;
    font-size: 36px;
    color: var(--leaf-green);
  }
  .product-type {
    position: absolute;
    top: 770px;
    left: 95px;
    width: 540px;
    height: 90px;
    border-top: 2px solid var(--rule-yellow);
    border-bottom: 2px solid var(--rule-yellow);
    display: flex;
    align-items: center;
    justify-content: center;
    font-family: "Roboto Condensed", sans-serif;
    font-weight: 400;
    font-size: 50px;
    letter-spacing: 1px;
    color: var(--ink-white);
  }
  .description {
    position: absolute;
    top: 885px;
    left: 130px;
    width: 470px;
    font-family: "Roboto Condensed", sans-serif;
    font-weight: 300;
    font-size: 18px;
    line-height: 1.75;
    color: var(--body-grey);
  }
  .tagline {
    position: absolute;
    top: 1080px;
    left: 0;
    width: 100%;
    font-family: "Playfair Display", serif;
    font-weight: 900;
    font-size: 26px;
    letter-spacing: 1px;
    color: var(--aloha-yellow);
  }
  .volume {
    position: absolute;
    top: 1125px;
    left: 0;
    width: 100%;
    display: flex;
    justify-content: center;
    align-items: center;
    gap: 18px;
    font-family: "Roboto Condensed", sans-serif;
    font-weight: 400;
    font-size: 24px;
    color: var(--ink-white);
  }
  .volume__rule {
    width: 50px;
    height: 2px;
    background: var(--rule-yellow);
  }
</style>
</head>
<body>
  <main class="label">
    <h1 class="wordmark">
      <span class="wordmark__natural">Natural</span>
      <span class="wordmark__line">PEST</span>
      <span class="wordmark__line wordmark__line--small">WARD</span>
    </h1>

    <div class="brand-mark">
      <span class="brand-mark__square"></span>
      <span class="brand-mark__name">The Grove</span>
    </div>

    <p class="claim">Deet Free</p>

    <h2 class="product-type">BUG SPRAY</h2>

    <p class="description">Natural Bug Spray enriched with quality essential oils that repels mosquitos, gnats, no seeums, ticks and all other bitey things.</p>

    <p class="tagline">MADE WITH ALOHA</p>

    <p class="volume">
      <span class="volume__rule"></span>
      <span>4 FL OZ/ 118 mL</span>
      <span class="volume__rule"></span>
    </p>
  </main>
</body>
</html>
```